PSD website for property company

Please read the brief thoroughly.

We are looking for a new website for a property group that does property acquisitions, property development and property management.
They buy, build and lease core inner city industrial assets in Sydney, Australia.
They also invest in residential developments.

Site menu
- Home page
- Property – sub menus include – Leasing ; Projects ; Investments ; Property Management
- Capital and finance
- About
- Contact

They like this website
https://www.velmorn.com.au/

They want the site to be clean, modern and bold.
They like few colors, even black and white is OK to submit

They have a logo and style guide and useable images here:
http://www.quorvex.net/temp/PellikWeb2019.zip
The zip file is also attached to this project.
We have supplied some images to give you an idea, but we will also require you to provide at least 3 extra images from stock photos.
Use your imagination.

I am expecting a lot of similar designs, so be aware the photos you choose will be really important.
They want really 3 good stock photos used and supplied without charge.
Please not too generic, I repeat the quality of the photos is important.
You may provide several photos (but not in multiple submissions please) and we will choose the best three to be provided.

The winner will be selected on a single home page design and required to provide;
All photos use in original format without charge
A second ‘standard page’ template design based on the winning home page design

```html
<!DOCTYPE html>
<html lang="en">
<head>
<meta charset="utf-8">
<title>Pellik – Contact &amp; Enquire</title>
<link rel="stylesheet" href="https://fonts.googleapis.com/css2?family=Cabin:wght@400;500;600;700&family=Lato:ital,wght@1,400&display=swap">
<style>
  :root {
    --orange: #de9e52;
    --white: #ffffff;
    --panel-light: #f6f6f6;
    --ink: #2b2b2b;
    --divider: rgba(255,255,255,0.45);
  }
  * { box-sizing: border-box; margin: 0; padding: 0; }
  html, body { width: 1200px; height: 622px; overflow: hidden; background: var(--white); }
  body { position: relative; font-family: "Cabin", sans-serif; }

  .contact-panel {
    position: absolute; left: 161px; top: 0; width: 438px; height: 622px;
    background: var(--orange); color: var(--white); text-align: center;
  }
  .enquire-panel {
    position: absolute; left: 599px; top: 0; width: 440px; height: 622px;
    background: var(--panel-light); text-align: center;
  }
  .section-title {
    position: absolute; left: 0; right: 0; top: 53px;
    font-size: 27px; font-weight: 500; letter-spacing: 3.5px; line-height: 34px;
  }
  .enquire-panel .section-title { color: var(--orange); }

  .contact-intro {
    position: absolute; left: 0; right: 0; top: 103px;
    font-size: 10.5px; line-height: 22.5px; letter-spacing: 1px; white-space: nowrap;
  }
  .divider {
    position: absolute; left: 144px; width: 150px; height: 1px; background: var(--divider);
  }
  .divider-top { top: 242px; }
  .divider-bottom { top: 478px; }

  .company-name {
    position: absolute; left: 0; right: 0; top: 267px;
    font-size: 26px; font-weight: 500; letter-spacing: 3.5px; line-height: 34px;
  }
  .company-details {
    position: absolute; left: 0; right: 0; top: 317px;
    list-style: none; font-size: 10.5px; line-height: 22.5px; letter-spacing: 1px;
  }
  .company-details strong { font-weight: 700; letter-spacing: 1.2px; }

  .social-links {
    position: absolute; top: 509px; left: 0; right: 0;
    display: flex; justify-content: center; gap: 11px;
  }
  .social-link {
    width: 53px; height: 53px; background: var(--white); border-radius: 2px;
    display: flex; align-items: center; justify-content: center;
    color: var(--orange); font-size: 8px; font-weight: 600; letter-spacing: 0.3px;
    text-decoration: none;
  }

  .enquiry-form { position: absolute; left: 60px; top: 110px; width: 320px; }
  .field {
    display: block; width: 320px; height: 52px; margin-bottom: 12px;
    border: 1.5px solid var(--orange); background: transparent;
    padding-left: 15px; text-align: left;
    font-family: "Lato", sans-serif; font-style: italic; font-size: 11.5px;
    line-height: 49px; color: var(--ink);
  }
  .interest-label {
    position: absolute; top: 264px; left: 0; right: 0; line-height: 14px;
    font-size: 10.5px; letter-spacing: 1.5px; color: var(--ink);
  }
  .interest-options {
    position: absolute; top: 286px; left: 0; width: 320px;
    display: flex; justify-content: space-between;
  }
  .interest-option {
    width: 99px; height: 52px; border: 1.5px solid var(--orange);
    display: flex; align-items: center; justify-content: center;
    font-size: 10px; letter-spacing: 1.8px; font-weight: 500; color: var(--ink);
  }
  .consent {
    position: absolute; top: 361px; left: 1px; width: 320px;
    display: flex; align-items: center; gap: 4px;
    font-family: "Lato", sans-serif; font-style: italic; font-size: 6.4px; color: var(--ink);
    white-space: nowrap;
  }
  .consent-box { width: 8px; height: 8px; border: 1px solid #9a9a9a; background: var(--white); flex: none; }
  .submit-button {
    position: absolute; top: 399px; left: 59px; width: 202px; height: 52px;
    background: var(--orange); color: var(--white); border: none;
    font-family: "Cabin", sans-serif; font-size: 12px; font-weight: 600;
    display: flex; align-items: center; justify-content: center;
  }
</style>
</head>
<body>
  <section class="contact-panel">
    <h2 class="section-title">CONTACT</h2>
    <p class="contact-intro">Contact us for a consultation. Our experts are happy to<br>answer all of your questions and find the best possible<br>solution for the project you are working on and we are<br>looking forward to make everything easier for your job and<br>other requirements</p>
    <div class="divider divider-top"></div>
    <h3 class="company-name">PELLIK</h3>
    <ul class="company-details">
      <li>Street 18, Avenue 45 - 123</li>
      <li>Sydney, AUSTRALIA</li>
      <li>Phone: <strong>123 - 456 - 789</strong></li>
      <li>Fax: <strong>123 - 456 - 789</strong></li>
      <li>E-mail Address: <strong>site@example.com</strong></li>
      <li>E-mail Address: <strong>site@example.com</strong></li>
    </ul>
    <div class="divider divider-bottom"></div>
    <nav class="social-links">
      <a class="social-link" href="#">Frendo</a>
      <a class="social-link" href="#">Chirpa</a>
      <a class="social-link" href="#">Netlio</a>
    </nav>
  </section>

  <section class="enquire-panel">
    <h2 class="section-title">ENQUIRE</h2>
    <div class="enquiry-form">
      <div class="field">Your Name Here*</div>
      <div class="field">Phone Number Here*</div>
      <div class="field">E-Mail Address Here Here*</div>
      <div class="field">Your Name Here*</div>
      <p class="interest-label">I'm interested in:</p>
      <div class="interest-options">
        <span class="interest-option">BUYING</span>
        <span class="interest-option">LEASING</span>
        <span class="interest-option">INVESTING</span>
      </div>
      <label class="consent"><span class="consent-box"></span>I agree that my submitted data is being collected and stored and lorem ipsum dolor amet ningun</label>
      <div class="submit-button">SUBMIT MESSAGE</div>
    </div>
  </section>
</body>
</html>
```